Web design concept for a IT recruitment agency.

Our website addresses two different target groups:
- Customers (companies) wanting to hire new IT talent
- It talent to find a new JOB

We a looking for a visual design concept that either addresses both target groups in one of the following options:
a. target both groups in 1 single splash page.
b. target both groups in 2 different pages one for both groups
c. or any creative third concept you can come up with

Requirements, we want one overall visual concept, that both target groups can relate to.

Trigger words what we want to express:
- passion / drive
- knowhow
- involvement
- professional/yet playful
- engagement

Background, company culture:
We are a recruitment agency with over 15 years of experience, we have no hard-sale culture.
But we emphasize on long term relationships, showing real interest in people and their needs.

Design requirements:
Use logo
Flat contemporary design

Target Market(s)

Industry/Entity Type

Hire

Number of Pages Required

2 page

Requirements
Must have
• We a looking for a visual design concept that either addresses both target groups

```html
<!DOCTYPE html>
<html lang="en">
<head>
<meta charset="utf-8">
<title>Brightwell Reach – IT Recruitment</title>
<link href="https://fonts.googleapis.com/css2?family=Open+Sans:wght@400;600;700&family=Dancing+Script:wght@600&display=swap" rel="stylesheet">
<style>
:root{
  --blue:#0fa3e3;
  --blue-dark:#0b8fcb;
  --navy:#163f52;
  --ink:#333;
  --muted:#555;
  --grey-btn:#d4d4d4;
  --light-blue:#a9def4;
  --card-grey:#eef0f2;
  --footer:#1c1c1c;
  --footer-text:#bbb;
  --green:#6aa832;
  --orange:#f08a24;
}
*{box-sizing:border-box;margin:0;padding:0}
html,body{width:1200px;height:2786px;overflow:hidden}
body{font-family:"Open Sans",Arial,sans-serif;color:var(--ink);background:#fff;position:relative}
.abs{position:absolute}

/* header */
.site-header{position:absolute;top:0;left:0;width:1200px;height:120px;background:#fff;border-top:4px solid var(--blue);z-index:3}
.brand{position:absolute;left:84px;top:0;width:168px;height:176px;background:#fff;border-radius:0 0 84px 84px;display:flex;flex-direction:column;align-items:center;justify-content:center;gap:8px;box-shadow:0 3px 6px rgba(0,0,0,.15)}
.brand-dot{width:40px;height:40px;border-radius:50%;background:var(--blue)}
.brand-name{font-size:21px;font-weight:600;color:var(--navy);text-align:center;line-height:1.15}
.top-actions{position:absolute;right:80px;top:0;display:flex;height:46px}
.btn-upload{background:#e9e9e9;color:#444;font-size:16px;width:170px;display:flex;align-items:center;justify-content:center;gap:8px}
.btn-employee{background:var(--blue);color:#fff;width:150px;text-align:center;padding-top:4px;line-height:1.2}
.btn-employee b{font-size:16px;display:block}
.btn-employee small{font-size:10px;text-transform:uppercase}
.main-nav{position:absolute;right:80px;top:78px;display:flex;gap:28px;font-size:16px;color:#444}
.main-nav .active{color:var(--blue)}

/* hero */
.hero{position:absolute;top:120px;left:0;width:1200px;height:576px;background:radial-gradient(ellipse at 55% 35%,#7f8c97 0%,#4c5862 45%,#262d33 100%)}
.hero-title{position:absolute;top:238px;width:100%;text-align:center;font-family:"Dancing Script",cursive;font-size:64px;color:#fff}
.hero-lead{position:absolute;top:314px;left:130px;width:940px;text-align:center;color:#f2f2f2;font-size:20px;line-height:1.4}
.search-bar{position:absolute;top:373px;left:140px;width:912px;height:62px;background:rgba(255,255,255,.35);padding:6px;display:flex;gap:8px}
.field{background:#fff;height:50px;display:flex;align-items:center;padding-left:16px;gap:10px;color:#888;font-size:14px}
.btn-search{background:var(--blue);color:#fff;font-size:22px;font-weight:600;flex:1;display:flex;align-items:center;justify-content:center}
.browse{position:absolute;top:466px;width:100%;text-align:center;color:#fff;font-size:14px}

/* intro */
.intro{position:absolute;top:696px;left:0;width:1200px;height:362px;background:linear-gradient(160deg,#e6f4fb 0%,#fff 35%,#fff 65%,#e6f4fb 100%)}
.intro h1{position:absolute;top:44px;width:100%;text-align:center;font-weight:400;font-size:40px;color:#333}
.intro-rule{position:absolute;top:100px;left:200px;width:800px;height:4px;background:linear-gradient(90deg,var(--navy) 0 20%,var(--blue) 20% 40%,#ddd 40% 45%,var(--navy) 45% 70%,var(--blue) 70% 100%)}
.intro-swirl{position:absolute;top:72px;width:38px;height:38px;border-radius:50%;border:6px solid var(--blue)}
.intro p{position:absolute;left:88px;width:1024px;text-align:center;font-size:12.5px;line-height:1.75;color:#444}

/* jobs */
.jobs{position:absolute;top:1058px;left:0;width:1200px;height:810px;background:linear-gradient(135deg,#c8ebfa 0%,#9fdaf3 50%,#b9e6f8 100%);border-top:3px solid var(--navy)}
.tab{position:absolute;top:28px;height:42px;width:240px;font-size:24px;text-align:center;line-height:42px}
.tab-find{left:346px;background:#fff;color:#333}
.tab-post{left:614px;background:var(--navy);color:#fff}
.job-board{position:absolute;top:70px;left:80px;width:1040px;height:689px;background:#fff}
.filters{position:absolute;top:36px;left:36px;display:flex;gap:18px}
.filter{height:32px;padding:0 20px;font-size:13px;line-height:32px;background:var(--blue);color:#fff}
.filter.all{background:var(--grey-btn);color:#333;width:118px;text-align:center}
.job{position:absolute;width:450px;height:127px;border-bottom:1px solid #ddd}
.job-logo{position:absolute;left:0;top:14px;width:118px;height:92px;border:1px solid #ddd;box-shadow:0 1px 3px rgba(0,0,0,.2);display:flex;align-items:center;justify-content:center;font-size:17px;font-weight:700;color:#333}
.job-title{position:absolute;left:130px;top:18px;font-size:14px;color:var(--blue)}
.job-company{position:absolute;left:130px;top:40px;font-size:13.5px;color:#333}
.job-meta{position:absolute;left:130px;top:68px;font-size:12px;display:flex;gap:26px}
.job-meta .loc{color:var(--green)}
.job-meta .date{color:var(--orange)}
.job-meta span{display:flex;align-items:center;gap:5px}
.pager{position:absolute;top:638px;left:469px;display:flex;gap:26px}
.pager div{width:38px;height:30px;background:var(--blue);display:flex;align-items:center;justify-content:center}

/* features */
.features{position:absolute;top:1868px;left:0;width:1200px;height:442px;background:#fff}
.feature{position:absolute;top:112px;width:328px;height:227px;background:var(--card-grey);border:1px solid #ddd;text-align:center}
.feature-icon{position:absolute;top:-92px;left:86px;width:156px;height:156px;border-radius:50%;background:#fff;box-shadow:0 2px 4px rgba(0,0,0,.1);display:flex;align-items:center;justify-content:center}
.feature-icon div{width:138px;height:138px;border-radius:50%;background:var(--navy);display:flex;align-items:center;justify-content:center}
.feature h3{position:absolute;top:84px;width:100%;font-weight:400;font-size:18px;color:var(--blue-dark)}
.feature p{position:absolute;top:122px;left:24px;right:24px;font-size:13px;line-height:1.55;color:#333}
.feature .btn{position:absolute;top:209px;left:105px;width:118px;height:32px;line-height:30px;background:var(--blue);color:#fff;font-size:13px;border-bottom:3px solid var(--navy)}

/* partners */
.partners{position:absolute;top:2310px;left:0;width:1200px;height:165px;background:linear-gradient(#e3f4fc,#fff)}
.partners h2{position:absolute;top:28px;width:100%;text-align:center;font-weight:400;font-size:23px;color:var(--navy)}
.partner-row{position:absolute;top:94px;left:100px;display:flex;gap:0}
.partner{width:200px;height:40px;display:flex;align-items:center;justify-content:center;border-right:1px solid #ccc}
.partner span{display:block;width:140px;height:26px;background:#9aa3a8;border-radius:3px}

/* footer */
.site-footer{position:absolute;top:2475px;left:0;width:1200px;height:311px;background:var(--footer);color:var(--footer-text)}
.col{position:absolute;top:40px}
.col h4{font-weight:400;font-size:16px;color:#fff;margin-bottom:12px}
.col li{list-style:none;font-size:11px;line-height:26px}
.col li::before{content:"› "}
.newsletter p{font-size:11px;line-height:1.5;width:200px}
.email-field{margin-top:8px;width:200px;height:26px;background:#fff;color:#666;font-size:11px;padding:6px 8px}
.btn-subscribe{margin-top:10px;width:74px;height:22px;background:var(--orange);color:#fff;font-size:10px;text-align:center;line-height:22px}
.follow{margin-top:14px;font-size:16px;color:#fff}
.social{margin-top:10px;display:flex;gap:8px}
.social span{width:26px;height:26px;background:var(--blue)}
.copyright{position:absolute;top:277px;width:100%;text-align:center;font-size:11px;color:#999;border-top:1px solid #333;left:80px;width:1040px;padding-top:10px;top:266px}
</style>
</head>
<body>

<header class="site-header">
  <div class="brand"><span class="brand-dot"></span><span class="brand-name">Brightwell<br>Reach</span></div>
  <div class="top-actions">
    <div class="btn-upload">
      <svg width="26" height="18" viewBox="0 0 26 18"><path d="M6 17a5 5 0 0 1 0-10 7 7 0 0 1 13 1 4.5 4.5 0 0 1 0 9z" fill="#0fa3e3"/><path d="M13 6l-4 4h3v4h2v-4h3z" fill="#fff"/></svg>
      Upload Resume
    </div>
    <div class="btn-employee"><b>Employee ⌄</b><small>Looking to hire</small></div>
  </div>
  <nav class="main-nav">
    <span class="active">Home</span><span>Find Jobs</span><span>Post Resumes</span><span>My Profile</span><span>Career Advice</span><span>Blog</span><span>Contact</span>
  </nav>
</header>

<section class="hero" role="img" aria-label="Photo of a team of business professionals standing behind their leader">
  <div class="hero-title">Find Your Future With Brightwell Reach</div>
  <p class="hero-lead">We are a recruitment agency with over 15 years of experience. We emphasize on long term relationships, showing real interest in people and their needs.</p>
  <div class="search-bar">
    <div class="field" style="width:318px">
      <svg width="12" height="12" viewBox="0 0 12 12"><circle cx="5" cy="5" r="3.5" fill="none" stroke="#999" stroke-width="1.5"/><path d="M8 8l3 3" stroke="#999" stroke-width="1.5"/></svg>Job Title, Keywords</div>
    <div class="field" style="width:212px">
      <svg width="12" height="10" viewBox="0 0 12 10"><rect x="0" y="2" width="12" height="8" rx="1" fill="#999"/><rect x="4" y="0" width="4" height="3" fill="none" stroke="#999"/></svg>Exp (Years)</div>
    <div class="field" style="width:212px">
      <svg width="10" height="13" viewBox="0 0 10 13"><path d="M5 13S0 7 0 5a5 5 0 0 1 10 0c0 2-5 8-5 8z" fill="#999"/><circle cx="5" cy="5" r="1.8" fill="#fff"/></svg>Location</div>
    <div class="btn-search">SEARCH</div>
  </div>
  <p class="browse"><b>Browse Jobs:</b> Function | Industry | Location | Companies | Consultants | International | Government | Contract | Special Ability</p>
</section>

<section class="intro">
  <h1>Experts in IT jobs and IT recruitment</h1>
  <div class="intro-swirl" style="left:154px"></div>
  <div class="intro-rule"></div>
  <div class="intro-swirl" style="left:1004px"></div>
  <p style="top:144px">Lorem ipsum dolor sit amet, consectetur adipiscing elit. Integer sit amet metus neque. In eu lobortis diam, necLorem ipsum dolor sit amet, consectetur adipiscing elit. Integer sit amet metus neque. In eu lobortis diam, nec egestas augue. Maecenas id dolor consequat. Nunc risus risus, ullamcorper blandit sapien. Sed lectus lectus, laoreet at auctor sed, egestas sed odio. Nulla eget mattis nisi, eu pellentesque dolor. Ut fermentum nibh leo, et volutpat neque accumsan nec. Nulla eget mattis nisi, eu pellentesque dolor.</p>
  <p style="top:228px">Ut Donec vehicula rutrum dapibus. Suspendisse tortor purus, elementum eu tempus in, viverra eu lectus. Integer interdum luctus facilisis. Etiam pellentesque suscipit congue. fermentum nibh leo, et volutpat neque accumsan nec. Nam ac dui blandit, pellentesque ex nec, porta purus. Morbi risus risus, imperdiet eu vehicula nec, suscipit convallis nibh.</p>
</section>

<section class="jobs">
  <div class="tab tab-find">Find A Job</div>
  <div class="tab tab-post">Post A Job</div>
  <div class="job-board">
    <div class="filters">
      <div class="filter all">All Jobs</div>
      <div class="filter">Information Technology</div>
      <div class="filter">Manufacturing</div>
      <div class="filter">Other Jobs</div>
    </div>

    <div class="job" style="left:36px;top:98px"><div class="job-logo">Norvex</div><div class="job-title">Opening for an Executive - Cat...</div><div class="job-company">Intrabyte Systems Limited</div><div class="job-meta"><span class="loc">📍 Location: USA</span><span class="date">Posted on: 17/07/2015</span></div></div>
    <div class="job" style="left:554px;top:98px"><div class="job-logo" style="font-size:14px">Kestrel Infotech</div><div class="job-title">Urgent Opening for an Associat...</div><div class="job-company">Intrabyte Systems Limited</div><div class="job-meta"><span class="loc">📍 Location: USA</span><span class="date">Posted on: 17/07/2015</span></div></div>

    <div class="job" style="left:36px;top:225px"><div class="job-logo">Cobaltix</div><div class="job-title">Urgent Opening for an Associat...</div><div class="job-company">Intrabyte Systems Limited</div><div class="job-meta"><span class="loc">📍 Location: USA</span><span class="date">Posted on: 17/07/2015</span></div></div>
    <div class="job" style="left:554px;top:225px"><div class="job-logo">Harlow Bank</div><div class="job-title">Urgent Opening for an Associat...</div><div class="job-company">Intrabyte Systems Limited</div><div class="job-meta"><span class="loc">📍 Location: USA</span><span class="date">Posted on: 17/07/2015</span></div></div>

    <div class="job" style="left:36px;top:352px"><div class="job-logo">Tekmara</div><div class="job-title">Opening for an Executive - Cat...</div><div class="job-company">Intrabyte Systems Limited</div><div class="job-meta"><span class="loc">📍 Location: USA</span><span class="date">Posted on: 17/07/2015</span></div></div>
    <div class="job" style="left:554px;top:352px"><div class="job-logo">Perdura</div><div class="job-title">Chief Financial Officer</div><div class="job-company">Yara Labs</div><div class="job-meta"><span class="loc">📍 Location: USA</span><span class="date">Posted on: 17/07/2015</span></div></div>

    <div class="job" style="left:36px;top:479px"><div class="job-logo">Genlane</div><div class="job-title">Opening for Service Engineers ...</div><div class="job-company">KNL Systems Private Limited</div><div class="job-meta"><span class="loc">📍 Location: USA</span><span class="date">Posted on: 17/07/2015</span></div></div>
    <div class="job" style="left:554px;top:479px"><div class="job-logo">Arcentis</div><div class="job-title">Opening for an Executive - Cat...</div><div class="job-company">Intrabyte Systems Limited</div><div class="job-meta"><span class="loc">📍 Location: USA</span><span class="date">Posted on: 17/07/2015</span></div></div>

    <div class="pager">
      <div><svg width="10" height="14" viewBox="0 0 10 14"><path d="M8 1L2 7l6 6" fill="none" stroke="#fff" stroke-width="2"/></svg></div>
      <div><svg width="10" height="14" viewBox="0 0 10 14"><path d="M2 1l6 6-6 6" fill="none" stroke="#fff" stroke-width="2"/></svg></div>
    </div>
  </div>
</section>

<section class="features">
  <div class="feature" style="left:80px">
    <div class="feature-icon"><div>
      <svg width="54" height="66" viewBox="0 0 54 66"><rect x="2" y="2" width="50" height="62" rx="3" fill="none" stroke="#fff" stroke-width="3"/><circle cx="27" cy="20" r="6" fill="#fff"/><rect x="18" y="28" width="18" height="6" rx="3" fill="#fff"/><rect x="12" y="42" width="30" height="3" fill="#fff"/><rect x="12" y="50" width="30" height="3" fill="#fff"/></svg>
    </div></div>
    <h3>Send Us Your Resume</h3>
    <p>To connect with a great job opportunity, you have to take the first step. We can help you to choose the right job.</p>
    <div class="btn">Send</div>
  </div>
  <div class="feature" style="left:436px">
    <div class="feature-icon"><div>
      <svg width="70" height="70" viewBox="0 0 70 70"><circle cx="40" cy="30" r="22" fill="#fff"/><circle cx="40" cy="30" r="16" fill="#163f52"/><path d="M24 46L6 64" stroke="#fff" stroke-width="8" stroke-linecap="round"/></svg>
    </div></div>
    <h3>Brightwell Reach Is Everywhere</h3>
    <p>Our search to find the right talent for our clients. And also to place the right talent to right place.</p>
    <div class="btn">Learn More</div>
  </div>
  <div class="feature" style="left:792px">
    <div class="feature-icon"><div>
      <svg width="72" height="66" viewBox="0 0 72 66"><rect x="24" y="2" width="26" height="16" rx="4" fill="none" stroke="#fff" stroke-width="3"/><rect x="10" y="40" width="52" height="4" fill="#fff"/><rect x="34" y="44" width="4" height="20" fill="#fff"/><circle cx="10" cy="28" r="6" fill="#fff"/><circle cx="62" cy="28" r="6" fill="#fff"/></svg>
    </div></div>
    <h3>Career Advice</h3>
    <p>What career is right for you? We can help you to choose the right decision.</p>
    <div class="btn">Get Advice</div>
  </div>
</section>

<section class="partners">
  <h2>OUR CUSTOMERS AND PARTNERS</h2>
  <div class="partner-row">
    <div class="partner"><span></span></div>
    <div class="partner"><span></span></div>
    <div class="partner"><span></span></div>
    <div class="partner"><span></span></div>
    <div class="partner"><span></span></div>
  </div>
</section>

<footer class="site-footer">
  <div class="col" style="left:80px"><h4>COMPANY</h4><ul><li>About Us</li><li>Terms &amp; Conditions</li><li>Privacy Policy</li><li>Resources</li><li>Careers with Us</li><li>Sitemap</li><li>Contact Us</li></ul></div>
  <div class="col" style="left:263px"><h4>JOBSEEKERS</h4><ul><li>Register Now</li><li>Search Jobs</li><li>Login</li><li>Create Job Alert</li><li>Blogs</li><li>Security Advice</li></ul></div>
  <div class="col" style="left:476px"><h4>EMPLOYERS</h4><ul><li>Post Jobs</li><li>Access Database</li><li>Manage Responses</li><li>Buy Online</li><li>Report a Problem</li></ul></div>
  <div class="col" style="left:701px"><h4>BROWSE JOBS</h4><ul><li>Jobs by Category</li><li>Jobs by Company</li><li>Jobs by Skill</li><li>Jobs by Designation</li><li>Jobs by Location</li><li>Browse All Jobs</li></ul></div>
  <div class="col newsletter" style="left:915px"><h4>NEWSLETTER SIGNUP</h4>
    <p>Please enter your email address below to receive our FREE newsletter</p>
    <div class="email-field">Your Email ID</div>
    <div class="btn-subscribe">SUBSCRIBE</div>
    <div class="follow">FOLLOW US</div>
    <div class="social"><span></span><span></span><span></span><span></span></div>
  </div>
  <div class="copyright">Copyrights © 2015 Brightwell Reach. All rights reserved.</div>
</footer>

</body>
</html>
```